Convert Design into Adobe Ilustrator (Ai) File - Product Label

Convert the provided Graphic Design into an Adobe Illustrator (Ai) File for a Product Label. This Ai file needs to be fully editable, organised into logical layers and well structured. The text needs to be outlined for printing. This is for a POUCH DESIGN. The pouch dimensions file is attached. We'll share the details for the other side of the pouch if you are interested in accepting this project. Thanks.

Industry/Entity Type

FOOD SUPPLEMENTS

```html
<!DOCTYPE html>
<html lang="en">
<head>
<meta charset="UTF-8">
<title>Tide &amp; Tonic – Marine Collagen Complex Pouch Label</title>
<link rel="stylesheet" href="https://fonts.googleapis.com/css2?family=Cormorant+Garamond:wght@400;500;600&family=Tinos&display=swap">
<style>
  :root {
    --navy-deep: #14224a;
    --navy: #1d2f63;
    --navy-light: #26397a;
    --gold: #f0b774;
    --gold-soft: rgba(240, 183, 116, 0.55);
    --ivory: #f4f1ea;
    --rule: rgba(220, 205, 190, 0.6);
  }
  * { margin: 0; padding: 0; box-sizing: border-box; }
  html, body {
    width: 910px; height: 1200px; overflow: hidden;
    background: var(--navy-deep);
  }
  .label {
    position: relative;
    width: 910px; height: 1200px;
    overflow: hidden;
    background: radial-gradient(ellipse at 55% 20%, var(--navy-light) 0%, var(--navy) 45%, var(--navy-deep) 100%);
    color: var(--ivory);
    font-family: "Cormorant Garamond", Georgia, serif;
  }
  .wave-field {
    position: absolute; left: 0; right: 0; bottom: 0; height: 560px;
    background:
      radial-gradient(ellipse at 85% 55%, rgba(240,183,116,0.16) 0%, rgba(240,183,116,0) 55%),
      radial-gradient(ellipse at 15% 70%, rgba(120,145,210,0.14) 0%, rgba(120,145,210,0) 55%),
      linear-gradient(180deg, rgba(20,34,74,0) 0%, rgba(12,22,52,0.35) 100%);
  }
  .brand {
    position: absolute; top: 148px; left: 0; width: 910px;
    text-align: center;
    font-family: "Cormorant Garamond", Georgia, serif;
    font-weight: 500;
    font-size: 56px;
    letter-spacing: 0.2em;
    color: var(--gold);
    padding-left: 0.2em;
  }
  .brand-rule {
    position: absolute; top: 244px; left: 95px; width: 680px; height: 1px;
    background: var(--rule);
  }
  .product-title {
    position: absolute; top: 290px; left: 79px;
    font-family: "Cormorant Garamond", Georgia, serif;
    font-weight: 500;
    font-size: 78px;
    line-height: 57px;
    letter-spacing: -0.02em;
    color: var(--gold);
    transform: scaleY(1.12);
    transform-origin: top left;
  }
  .ingredients {
    position: absolute; top: 600px; left: 97px;
    font-family: "Cormorant Garamond", Georgia, serif;
    font-weight: 500;
    font-size: 35px;
    line-height: 45.5px;
    color: var(--ivory);
  }
  .serving-divider {
    position: absolute; top: 752px; left: 209px; width: 1px; height: 18px;
    background: var(--ivory);
  }
  .serving-info {
    position: absolute; top: 776px; left: 89px;
    font-family: "Tinos", "Times New Roman", serif;
    font-size: 17px;
    letter-spacing: -0.02em;
    color: var(--ivory);
    white-space: pre;
  }
  .claims { position: absolute; left: 0; top: 0; }
  .claim {
    position: absolute; left: 500px;
    display: flex; align-items: center;
    font-family: "Tinos", "Times New Roman", serif;
    font-size: 16px;
    line-height: 22px;
    letter-spacing: -0.02em;
    color: var(--ivory);
  }
  .claim svg { width: 56px; height: 56px; flex: none; margin-right: 17px; }
  .claim-icon { fill: none; stroke: var(--gold); stroke-width: 1.6; stroke-linecap: round; stroke-linejoin: round; }
  .claim--weight { top: 572px; }
  .claim--size { top: 644px; }
  .claim--flavour { top: 713px; }
  .claim--source { top: 783px; }
  .net-weight {
    position: absolute; top: 1142px; left: 0; width: 770px;
    text-align: center;
    font-family: "Tinos", "Times New Roman", serif;
    font-size: 18px;
    letter-spacing: -0.02em;
    color: var(--ivory);
  }
</style>
</head>
<body>
<main class="label">
  <div class="wave-field" role="img" aria-label="Flowing gold and blue contour wave lines across the lower half of the pouch"></div>

  <div class="brand">TIDE &amp; TONIC</div>
  <div class="brand-rule"></div>

  <h1 class="product-title">MARINE<br>COLLAGEN<br>COMPLEX</h1>

  <p class="ingredients">Marine Collagen,<br>Vitamin C<br>&amp; Hyaluronic Acid</p>
  <div class="serving-divider"></div>
  <p class="serving-info">30 servings  13.500mg per serving</p>

  <ul class="claims">
    <li class="claim claim--weight">
      <svg viewBox="0 0 56 56" aria-hidden="true">
        <circle class="claim-icon" cx="28" cy="28" r="21"/>
        <path class="claim-icon" d="M28 16 C20 24 20 32 28 40 C36 32 36 24 28 16 Z M28 22 V46"/>
      </svg>
      <span>Low molecular weight</span>
    </li>
    <li class="claim claim--size">
      <svg viewBox="0 0 56 56" aria-hidden="true">
        <path class="claim-icon" d="M28 6 C22 20 16 28 16 36 A12 12 0 0 0 40 36 C40 28 34 20 28 6 Z"/>
        <path class="claim-icon" d="M22 38 A6 6 0 0 0 34 38"/>
      </svg>
      <span>2000 kDa</span>
    </li>
    <li class="claim claim--flavour">
      <svg viewBox="0 0 56 56" aria-hidden="true">
        <path class="claim-icon" d="M14 46 C12 26 24 12 44 10 C46 30 34 44 14 46 Z M14 46 L36 20 M22 36 L30 36 M26 30 L24 24"/>
      </svg>
      <span>Unflavoured</span>
    </li>
    <li class="claim claim--source">
      <svg viewBox="0 0 56 56" aria-hidden="true">
        <path class="claim-icon" d="M12 24 C20 14 36 14 46 22 C36 30 20 30 12 20 M12 20 L6 14 M12 24 L6 28"/>
        <circle class="claim-icon" cx="39" cy="21" r="1.5"/>
        <path class="claim-icon" d="M6 38 Q12 34 18 38 T30 38 T42 38 M10 45 Q16 41 22 45 T34 45"/>
      </svg>
      <span>Sourced from<br>wild caught fish</span>
    </li>
  </ul>

  <p class="net-weight">Food Supplement e 375g</p>
</main>
</body>
</html>
```